Financial Advisor needs waiting room sign

I am a financial advisor that works with a number of accountants to develop prospects. I am looking for a 18"x24" sign to hang in their office waiting rooms to help develop prospect interest in my services. My original idea was to list all of our services in a jumbled way on the sign and on the bottom have something like "Confused? We have the answers?" "Questions - We have answers" Our logo on the bottom. While I think this is still a good idea when I try to design it - it does not work. I am open to other ideas. Here is a list of our services (list in no particular order) and I will attach our logo. List: Plovance, Plovance Supplement, Plovance Advantage, Truvely, Part A, Part B, Part D, Social Security, Turning 65, Annuities, Fixed Index Annuities, Rollovers, 401k, 403b, Investments, Stock Market, Mutual Funds, Term Insurance, Life Insurance, Final Expense, Long Term Care, Mortgage Protection, 403B / 457 Not for Profit Set Up, 403B / TSA Plans, Annuities, Asset Protection, Charitable Giving, College Funding, Estate Planning, Fixed Indexed Annuities, Guaranteed Income, IRA & 401(K) Assets and Planning, IRA, 401(K), 403(B) Rollovers, Lifetime Income Planning, Retirement Income Planning, Safe Money Options, Social Security, Tactical Asset Allocation

```html
<!DOCTYPE html>
<html lang="en">
<head>
<meta charset="utf-8">
<title>We have the answers – Brennick Capital</title>
<link href="https://fonts.googleapis.com/css2?family=Gelasio:wght@700&display=swap" rel="stylesheet">
<style>
  :root {
    --paper: #ffffff;
    --headline: #00ee0c;
    --headline-shadow: rgba(0, 0, 0, 0.45);
    --service-text: #555555;
    --brand: #4f7d12;
  }
  html, body {
    margin: 0;
    padding: 0;
    overflow: hidden;
  }
  .sign {
    position: relative;
    width: 900px;
    height: 1200px;
    background: var(--paper);
    overflow: hidden;
    font-family: "Gelasio", Georgia, serif;
    font-weight: 700;
  }
  .headline {
    position: absolute;
    top: 22px;
    left: 0;
    width: 100%;
    margin: 0;
    text-align: center;
    font-size: 56px;
    line-height: 1.2;
    color: var(--headline);
    text-shadow: 2px 2px 2px var(--headline-shadow);
    letter-spacing: 0.2px;
  }
  .service-list {
    position: absolute;
    top: 110px;
    left: 230px;
    margin: 0;
    padding: 0;
    list-style: none;
    font-size: 24px;
    line-height: 29.3px;
    color: var(--service-text);
  }
  .brand {
    position: absolute;
    top: 1100px;
    left: 243px;
    display: flex;
    align-items: center;
    gap: 18px;
  }
  .brand-mark {
    width: 54px;
    height: 54px;
    border-radius: 50%;
    background: var(--brand);
  }
  .brand-name {
    font-size: 30px;
    color: var(--brand);
    letter-spacing: 1px;
  }
</style>
</head>
<body>
  <main class="sign">
    <h1 class="headline">We have the answers</h1>
    <ul class="service-list">
      <li>Plovance,</li>
      <li>Plovance Supplement,</li>
      <li>Plovance Advantage,</li>
      <li>Truvely, Part A, Part B, Part D,</li>
      <li>Social Security,</li>
      <li>Turning 65,</li>
      <li>Annuities,</li>
      <li>Fixed Index Annuities,</li>
      <li>Rollovers, 401k, 403b,</li>
      <li>Investments, Stock</li>
      <li>Market,</li>
      <li>Mutual Funds,</li>
      <li>Term Insurance,</li>
      <li>Life Insurance,</li>
      <li>Final Expense,</li>
      <li>Long Term Care,</li>
      <li>Mortgage Protection,</li>
      <li>403B / 457 Not for Profit Set Up,</li>
      <li>403B / TSA Plans,</li>
      <li>Annuities,</li>
      <li>Asset Protection,</li>
      <li>Charitable Giving,</li>
      <li>College Funding,</li>
      <li>Estate Planning,</li>
      <li>Fixed Indexed Annuities,</li>
      <li>Guaranteed Income,</li>
      <li>IRA &amp; 401(K) Assets and Planning,</li>
      <li>IRA, 401(K), 403(B) Rollovers,</li>
      <li>Lifetime Income Planning,</li>
      <li>Retirement Income Planning,</li>
      <li>Safe Money Options, Social Security,</li>
      <li>Tactical Asset Allocation</li>
    </ul>
    <div class="brand">
      <span class="brand-mark" aria-hidden="true"></span>
      <span class="brand-name">Brennick Capital</span>
    </div>
  </main>
</body>
</html>
```